Venture firm needs flyer to attract Sales Professionals as Advisors

Creation of either a pdf Flyer or Brochure.
The target audience are senior sales professionals of the Information Technology industry. The flyer needs to come across highly professional, business oriented, positive. Text for the brochure is attached. The colors/graphics should align with Brindmore Capital corporate appearance: www.brindmore.capital

Target Market(s)

Sales Professionals in the Information Technology Industry

Industry/Entity Type

Information Technology

Font styles to use
• Raleway

Requirements
Must have
• fitting the corporate look and feel: www.brindmore.capital

```html
<!DOCTYPE html>
<html lang="en">
<head>
<meta charset="utf-8">
<title>Brindmore Sales Council Flyer</title>
<link href="https://fonts.googleapis.com/css2?family=Raleway:wght@300;400;600;700;800&family=Lato:wght@400;700&display=swap" rel="stylesheet">
<style>
:root{
  --navy:#1b416d;
  --navy-dark:#123154;
  --blue:#1d6fc2;
  --light-blue:#8fb7e3;
  --ink:#2a2a2a;
  --grey-band:#dfe3e8;
  --paper:#ffffff;
  --backdrop:#e9ecef;
}
*{box-sizing:border-box;margin:0;padding:0}
html,body{width:1200px;height:848px;overflow:hidden;background:var(--backdrop)}
.canvas{position:relative;width:1200px;height:848px}
.page{position:absolute;top:48px;width:540px;height:764px;background:var(--paper);overflow:hidden;box-shadow:0 2px 10px rgba(0,0,0,.15)}
.page--front{left:54px}
.page--back{left:618px}
.page svg.art{position:absolute;left:0;top:0}
.brand-box{position:absolute;background:var(--navy);display:flex;align-items:center;justify-content:center;font-family:"Raleway",sans-serif;font-weight:400;color:#fff;letter-spacing:.5px}
.brand-box--front{left:271px;top:34px;width:239px;height:44px;font-size:19px}
.brand-box--back{left:320px;top:27px;width:185px;height:35px;font-size:15px}
.title{position:absolute;right:30px;top:296px;text-align:right;font-family:"Raleway",sans-serif;line-height:1}
.title__top{display:block;color:var(--blue);font-weight:700;font-size:35px}
.title__main{display:block;color:var(--navy);font-weight:800;font-size:60px;margin-top:2px}
.title__sub{display:flex;align-items:center;justify-content:flex-end;gap:10px;color:var(--ink);font-weight:400;font-size:28px;margin-top:2px}
.title__sub::before{content:"";width:101px;height:6px;background:var(--blue)}
.intro{position:absolute;right:28px;top:460px;width:480px;text-align:right;font-family:"Lato",sans-serif;font-size:9.6px;line-height:1.35;color:var(--ink)}
.intro p{margin-bottom:6px}
.intro p:nth-child(1){padding-left:120px}
.intro p:nth-child(2){padding-left:40px}
.slogan{position:absolute;left:14px;top:612px;width:504px;height:41px;border:1.5px solid var(--blue);border-radius:12px;display:flex;align-items:center;justify-content:center;font-family:"Lato",sans-serif;font-weight:700;font-size:14.5px;color:var(--navy);box-shadow:0 1px 3px rgba(0,0,0,.15)}
.web-band{position:absolute;left:0;top:688px;width:318px;height:36px;background:var(--grey-band);text-align:center;font-family:"Lato",sans-serif;color:var(--ink)}
.web-band__label{font-size:9.5px;padding-top:5px}
.web-band__url{font-size:11px;letter-spacing:4px;margin-top:2px}
.contact{position:absolute;left:314px;top:672px;width:226px;height:76px;background:var(--navy);display:flex;padding:4px 6px;gap:8px;font-family:"Lato",sans-serif;color:#fff;font-size:7.2px;line-height:1.45}
.contact__col{flex:1}
.contact__col + .contact__col{border-left:1px solid rgba(255,255,255,.4);padding-left:6px}
.contact__region{display:block;width:32px;margin:0 auto 3px;text-align:center;background:var(--light-blue);color:var(--navy);font-size:6.5px}
.contact__line{display:flex;gap:3px;align-items:flex-start}
.contact__line svg{flex:none;margin-top:1.5px}
.how{position:absolute;left:28px;top:86px;width:484px;font-family:"Lato",sans-serif;font-size:9.1px;line-height:1.38;color:var(--ink)}
.how h2{font-family:"Raleway",sans-serif;font-weight:700;font-size:16px;color:var(--navy);margin-bottom:9px}
.how h3{font-family:"Raleway",sans-serif;font-weight:700;font-size:12px;color:var(--navy);margin:10px 0 6px}
.how p{margin-bottom:10px;text-align:justify}
.how p.tight{margin-bottom:0}
.how .closing{margin-left:130px;margin-top:6px}
.back-url{position:absolute;right:18px;bottom:14px;font-family:"Lato",sans-serif;font-size:11.5px;letter-spacing:4px;color:var(--navy)}
</style>
</head>
<body>
<main class="canvas">

  <section class="page page--front">
    <svg class="art" width="540" height="764" viewBox="0 0 540 764">
      <polygon role="img" aria-label="Photo of mountaineers roped together climbing a snowy ridge under a pale sky" points="0,150 52,104 540,104 540,168 0,548" fill="url(#snowPhoto)"/>
      <defs>
        <linearGradient id="snowPhoto" x1="0" y1="0" x2="1" y2="1">
          <stop offset="0" stop-color="#b89a6e"/>
          <stop offset=".35" stop-color="#d9e2ea"/>
          <stop offset=".7" stop-color="#7c8ea3"/>
          <stop offset="1" stop-color="#c8d6e4"/>
        </linearGradient>
      </defs>
      <polygon points="52,104 66,104 204,0 190,0 52,104 52,124 " fill="var(--navy)"/>
      <polygon points="52,104 200,0 258,0 66,125 52,125" fill="var(--navy)"/>
      <polygon points="0,548 540,164 540,178 0,562" fill="var(--navy)"/>
    </svg>

    <div class="brand-box brand-box--front">BRINDMORE CAPITAL</div>

    <h1 class="title">
      <span class="title__top">Brindmore</span>
      <span class="title__main">Sales</span>
      <span class="title__sub">Council</span>
    </h1>

    <div class="intro">
      <p>The BSC is a by invitation only global community of high caliber Sales Professionals in the IT industry. Participating in the BSC provides significant wealth creation opportunities by earning consulting fees and sales commission or finding an exciting startup to work for.</p>
      <p>BSC members actively collaborate with each other to close deals, generate leads &amp; opportunities, navigate through client organizations and build a true advisory status with customers.</p>
      <p>BSC members get early first hand visibility into the latest technology innovations and learn how those technologies could assist their clients in solving their complex business objectives.</p>
    </div>

    <div class="slogan">If you don´t get it right from the start it will just get harder as you grow!</div>

    <div class="web-band">
      <div class="web-band__label">For more info please visit our web:</div>
      <div class="web-band__url">www.brindmore.capital</div>
    </div>

    <div class="contact">
      <div class="contact__col">
        <span class="contact__region">USA</span>
        <div class="contact__line"><svg width="6" height="6" viewBox="0 0 6 6"><path d="M0 3 3 0 6 3V6H0Z" fill="#fff"/></svg><span>48 Harlow Ave.<br>Palo Verde, CA 94000</span></div>
        <div class="contact__line"><svg width="6" height="5" viewBox="0 0 6 5"><rect width="6" height="5" fill="#fff"/></svg><span>info@brindmore.capital</span></div>
        <div class="contact__line"><svg width="6" height="6" viewBox="0 0 6 6"><path d="M1 0 2.5 1.5 1.8 2.5Q3 4 3.8 4.2L4.5 3.5 6 5 5 6Q1 5 0 1Z" fill="#fff"/></svg><span>+1-555-014 2280</span></div>
      </div>
      <div class="contact__col">
        <span class="contact__region">Europe</span>
        <div class="contact__line"><svg width="6" height="6" viewBox="0 0 6 6"><path d="M0 3 3 0 6 3V6H0Z" fill="#fff"/></svg><span>Lindenweg 7<br>10100 Berlin - Germany</span></div>
        <div class="contact__line"><svg width="6" height="5" viewBox="0 0 6 5"><rect width="6" height="5" fill="#fff"/></svg><span>info@brindmore.capital</span></div>
        <div class="contact__line"><svg width="6" height="6" viewBox="0 0 6 6"><path d="M1 0 2.5 1.5 1.8 2.5Q3 4 3.8 4.2L4.5 3.5 6 5 5 6Q1 5 0 1Z" fill="#fff"/></svg><span>+49 170 0001 234</span></div>
      </div>
    </div>
  </section>

  <section class="page page--back">
    <svg class="art" width="540" height="764" viewBox="0 0 540 764">
      <defs>
        <linearGradient id="skiPhoto" x1="0" y1="0" x2="1" y2="1">
          <stop offset="0" stop-color="#9bb8d6"/>
          <stop offset=".45" stop-color="#e6edf4"/>
          <stop offset=".75" stop-color="#d6548a"/>
          <stop offset="1" stop-color="#3f6fa8"/>
        </linearGradient>
        <linearGradient id="hexPhoto" x1="0" y1="0" x2="0" y2="1">
          <stop offset="0" stop-color="#cfe0f1"/>
          <stop offset="1" stop-color="#5a4a40"/>
        </linearGradient>
      </defs>
      <polygon role="img" aria-label="Photo of a cheerful group of skiers in helmets and goggles posing in the snowy mountains" points="0,464 480,590 540,590 540,764 0,764" fill="url(#skiPhoto)"/>
      <polygon points="0,366 540,500 540,518 0,384" fill="var(--navy)" opacity=".0"/>
      <polygon points="0,366 360,452 360,470 0,382" fill="var(--navy)"/>
      <polygon points="140,714 330,764 140,764" fill="var(--navy)"/>
      <polygon role="img" aria-label="Photo of one climber helping another up onto a boulder" points="410,392 474,420 494,484 460,542 394,552 350,500 362,430" fill="url(#hexPhoto)" stroke="var(--blue)" stroke-width="5"/>
    </svg>

    <div class="brand-box brand-box--back">BRINDMORE CAPITAL</div>

    <div class="how">
      <h2>How it works:</h2>
      <p>BSC members will be introduced to Brindmore Capital' client and portfolio companies. This unique ability to learn about latest technology innovation keeps the participants up to date with industry trends and could open interesting earning or employment opportunities.</p>
      <p>Once exposed to a specific vendor, BSC members can decide if and how they would like to get further involved. Dependent on the interest level for the specific technology, the ability to offer a solution to a known customer problem or the sheer interest to develop new business, BSC members can participate in two ways:</p>
      <h3>* As Associates:</h3>
      <p>Associates are actively selling and promoting one or more Brindmore Capital´ portfolio companies. This could be an employment or a freelance opportunity.</p>
      <h3>* As Advisors:</h3>
      <p class="tight">Advisors offer their contacts and knowledge about customers to Associates.<br>Advisors could create leads, support with introductions, explain customer organization and processes etc. They will be compensated by Associates with a pre-negotiated % of commission of a future sale that was supported by the Advisor.</p>
      <p class="closing">Whatever level of involvement a BSC member seeks there is plenty of opportunity to be rewarded for working with fellow Sales Professionals and Great Startups on the forefront of technical innovation.</p>
    </div>

    <div class="back-url">www.brindmore.capital</div>
  </section>

</main>
</body>
</html>
```